Business Card and Letterhead for Nurlo - modern real estate business

I need a double sided business card design for Nurlo. Please see business card brief here https://papers.trelvimo.net/sheet/q/7XrTbaLeZpMmQ2uWvd9HkCj4yNoEfsGi3lRtAz_pk/view?mode=shared

Please feel free to design the business cards however you feel best. I am happy to give some creative freedoms and then provide feedback from there.

Please then also create a letterhead to match the business card design

Colors

Designer to choose colors to be used in the design.

Requirements
Must have
• Must be a modern, elegant business card which looks very professional

```html
<!DOCTYPE html>
<html lang="en">
<head>
<meta charset="utf-8">
<title>Nurlo – Business Card</title>
<link rel="stylesheet" href="https://fonts.googleapis.com/css2?family=Michroma&family=Open+Sans:wght@300;400&display=swap">
<style>
  :root {
    --page: #dcdcdc;
    --card: #121213;
    --red: #e31c25;
    --red-deep: #c41a22;
    --red-dark: #a8161d;
    --graphite: #3a3a3c;
    --text: #ffffff;
    --text-soft: #e6e6e6;
  }
  * { box-sizing: border-box; margin: 0; padding: 0; }
  html, body { width: 905px; height: 1200px; overflow: hidden; }
  body {
    background: var(--page);
    position: relative;
    font-family: "Open Sans", Arial, sans-serif;
    color: var(--text);
  }
  .card {
    position: absolute;
    width: 546px;
    height: 337px;
    background: var(--card);
    overflow: hidden;
  }
  .card--front { left: 177px; top: 193px; }
  .card--back { left: 185px; top: 630px; }
  .card__shapes { position: absolute; inset: 0; width: 100%; height: 100%; }

  .wordmark {
    position: absolute;
    font-family: "Michroma", "Arial Black", sans-serif;
    color: var(--red);
    font-weight: 400;
    line-height: 1;
    white-space: nowrap;
  }
  .card--front .wordmark { right: 48px; top: 84px; font-size: 50px; letter-spacing: 2px; }
  .card--back .wordmark { left: 0; right: 0; text-align: center; top: 140px; font-size: 62px; letter-spacing: 3px; }

  .portrait {
    position: absolute;
    left: 21px; top: 174px;
    width: 120px; height: 120px;
    border-radius: 22px;
    background: linear-gradient(135deg, #7d8a6a 0%, #b7c1b8 45%, #4c4a48 70%, #1e1e20 100%);
  }

  .agent { position: absolute; left: 159px; top: 183px; }
  .agent__name {
    font-family: "Michroma", "Arial Black", sans-serif;
    font-size: 16px;
    letter-spacing: 0.5px;
    line-height: 1;
  }
  .agent__role { font-size: 12px; font-weight: 300; margin-top: 5px; color: var(--text-soft); }

  .contact {
    position: absolute;
    top: 232px;
    font-size: 12px;
    font-weight: 300;
    line-height: 15.8px;
    color: var(--text-soft);
  }
  .contact--direct { left: 159px; }
  .contact--office { right: 46px; text-align: right; }

  .site {
    position: absolute;
    left: 0; right: 0; top: 226px;
    text-align: center;
    font-size: 15px;
    font-weight: 300;
    color: var(--text-soft);
  }
  .site__rule {
    display: block;
    width: 125px;
    height: 1px;
    margin: 0 auto;
    background: linear-gradient(90deg, transparent, #cfcfcf, transparent);
  }
  .site__text { display: block; padding: 4px 0 6px; }
</style>
</head>
<body>

<section class="card card--front" aria-label="Business card front">
  <svg class="card__shapes" viewBox="0 0 546 337" aria-hidden="true">
    <defs>
      <linearGradient id="frontTopGrey" x1="0" y1="0" x2="1" y2="0">
        <stop offset="0" stop-color="#4a4a4c"/>
        <stop offset="1" stop-color="#121213"/>
      </linearGradient>
      <linearGradient id="frontBand" x1="0" y1="0" x2="1" y2="0">
        <stop offset="0" stop-color="#2c2c2e"/>
        <stop offset="0.5" stop-color="#1a1a1b"/>
        <stop offset="1" stop-color="#121213"/>
      </linearGradient>
      <linearGradient id="frontBandRed" x1="0" y1="0" x2="1" y2="0">
        <stop offset="0" stop-color="#e31c25"/>
        <stop offset="0.35" stop-color="#b81820"/>
        <stop offset="0.65" stop-color="#e31c25"/>
        <stop offset="1" stop-color="#b51a20"/>
      </linearGradient>
    </defs>
    <polygon points="154,35 430,0 189,0" fill="url(#frontTopGrey)"/>
    <polygon points="0,0 189,0 0,189" fill="var(--red)"/>
    <polygon points="0,0 154,0 0,122" fill="var(--red-deep)"/>
    <polygon points="0,0 154,0 0,122" fill="var(--red)" opacity="0.6"/>
    <polygon points="0,0 44,0 0,45" fill="var(--red-dark)" opacity="0.7"/>
    <rect x="0" y="314" width="546" height="23" fill="url(#frontBand)"/>
    <polygon points="124,337 278,314 546,314 546,337" fill="url(#frontBandRed)"/>
    <polygon points="360,337 546,323 546,337" fill="var(--red)"/>
  </svg>

  <div class="wordmark">NURLO</div>

  <div class="portrait" role="img" aria-label="Portrait photo of the agent"></div>

  <div class="agent">
    <h1 class="agent__name">LIAM CARVER</h1>
    <p class="agent__role">Licenced Real Estate Agent</p>
  </div>

  <p class="contact contact--direct">0491 570 318<br>1300 654 982<br>liam@nurlo.com</p>
  <p class="contact contact--office">PO Box 7136<br>Ferncliff NSW 2790<br>www.nurlo.com</p>
</section>

<section class="card card--back" aria-label="Business card back">
  <svg class="card__shapes" viewBox="0 0 546 337" aria-hidden="true">
    <defs>
      <linearGradient id="backGrey" x1="0" y1="0" x2="1" y2="0">
        <stop offset="0" stop-color="#121213"/>
        <stop offset="1" stop-color="#4a4a4c"/>
      </linearGradient>
    </defs>
    <polygon points="86,337 385,299 348,337" fill="url(#backGrey)"/>
    <polygon points="546,139 546,337 348,337" fill="var(--red-deep)"/>
    <polygon points="546,206 546,337 381,337" fill="var(--red)"/>
    <polygon points="546,284 546,337 492,337" fill="var(--red)" opacity="0.9"/>
  </svg>

  <div class="wordmark">NURLO</div>

  <p class="site">
    <span class="site__rule"></span>
    <span class="site__text">www.nurlo.com</span>
    <span class="site__rule"></span>
  </p>
</section>

</body>
</html>
```